Presentation Folder for Brisk Estates

We are a new property management / real estate company in Denver Colorado and are in need of new stationary design. Attached are our business card and logo deigns. We are looking for our stationary design. We need a presentation folder design that is Professional, exciting, and approachable. We do not have a preference on folder layout (pockets, style of folding) but will most likely be using a standard two pocket folder design (roughly 9x12) but feel free to experiment with and folder style as long as we can find a place to print them. We would also like to have a matching letterhead/page design
Below is standard size of folder from lumo press
Full Bleed Size
20.87" x 16.68"
53 x 42.4 cm
6260 x 5004 pixels
Document Trim Size
20.75" x 16.56"
52.7 x 42.1 cm
6225 x 4969 pixels
Target Market(s)
We are attempting to target the top end of the real estate market in Denver Colorado. Are target market is investors in real estate.
Industry/Entity Type
Property Management
Font styles to use
Other font styles liked:
- Would like to keep font same to logo
Look and feel
Each slider illustrates characteristics of the customer's brand and the style your logo design should communicate.

```html
<!DOCTYPE html>
<html lang="en">
<head>
<meta charset="utf-8">
<title>Brisk Estates Presentation Folder</title>
<link href="https://fonts.googleapis.com/css2?family=Oswald:wght@400&family=Open+Sans:wght@400;600&display=swap" rel="stylesheet">
<style>
  :root{
    --bg:#e6e7e9;
    --paper:#f4f4f4;
    --paper-shade:#e9e9ea;
    --ink:#55575b;
    --ink-soft:#8a8c90;
    --sky:#8fbcd6;
    --sky-light:#b9d6e6;
    --sky-deep:#6fa6c6;
  }
  *{margin:0;padding:0;box-sizing:border-box}
  html,body{width:1200px;height:913px;overflow:hidden;background:var(--bg)}
  .stage{position:relative;width:1200px;height:913px}
  .spread{position:absolute;left:290px;width:620px;height:413px;background:var(--paper);
    box-shadow:0 2px 8px rgba(0,0,0,.18);overflow:hidden}
  .spread--outside{top:28px}
  .spread--inside{top:471px}
  .spread svg{position:absolute;inset:0}
  .wordmark{position:absolute;display:flex;align-items:center;gap:6px}
  .wordmark__dot{border-radius:50%;background:var(--sky)}
  .wordmark__name{font-family:"Oswald",sans-serif;font-weight:400;color:var(--ink);
    text-transform:uppercase;letter-spacing:.3px;line-height:1}
  .wordmark__tag{font-family:"Open Sans",sans-serif;color:var(--ink-soft);line-height:1.2}
  .wordmark--cover{top:40px;right:26px}
  .wordmark--cover .wordmark__dot{width:34px;height:34px}
  .wordmark--cover .wordmark__name{font-size:22px}
  .wordmark--cover .wordmark__tag{font-size:7px}
  .wordmark--small .wordmark__dot{width:20px;height:20px}
  .wordmark--small .wordmark__name{font-size:13px}
  .wordmark--small .wordmark__tag{font-size:4.5px}
  .wordmark--back{left:24px;bottom:18px}
  .wordmark--pocket{left:56px;bottom:36px}
  .wordmark--pocket .wordmark__dot{width:30px;height:30px}
  .wordmark--pocket .wordmark__name{font-size:18px}
  .wordmark--pocket .wordmark__tag{font-size:6px}
  .contact{position:absolute;bottom:18px;font-family:"Open Sans",sans-serif;font-size:4.5px;
    color:var(--ink-soft);line-height:1.6}
  .contact strong{font-weight:600;color:var(--ink)}
  .contact--postal{left:156px}
  .contact--lines{left:214px}
  .contact--web{left:340px}
</style>
</head>
<body>
<main class="stage">
  <section class="spread spread--outside" aria-label="Folder outside spread">
    <svg width="620" height="413" viewBox="0 0 620 413">
      <polygon class="band" points="620,250 620,413 470,413" fill="var(--sky-light)"/>
      <polygon class="band band--deep" points="620,300 620,413 530,413" fill="var(--sky)"/>
    </svg>
    <div class="wordmark wordmark--cover">
      <span class="wordmark__dot"></span>
      <div>
        <div class="wordmark__name">Brisk Estates</div>
        <div class="wordmark__tag">Property Management and Real Estate</div>
      </div>
    </div>
    <div class="wordmark wordmark--small wordmark--back">
      <span class="wordmark__dot"></span>
      <div>
        <div class="wordmark__name">Brisk Estates</div>
        <div class="wordmark__tag">Property Management and Real Estate</div>
      </div>
    </div>
    <div class="contact contact--postal"><strong>BRISK ESTATES</strong><br>P.O. Box 4410<br>Denver, CO 80201</div>
    <div class="contact contact--lines">(720) 555-0142<br>(720) 555-0178<br>info@briskestatesco.com</div>
    <div class="contact contact--web">www.briskestatesco.com</div>
  </section>

  <section class="spread spread--inside" aria-label="Folder inside spread">
    <svg width="620" height="413" viewBox="0 0 620 413">
      <line x1="310" y1="0" x2="310" y2="413" stroke="var(--paper-shade)" stroke-width="2"/>
      <path class="pocket" d="M0 310 H240 Q252 310 254 322 L262 413 H0 Z" fill="var(--paper-shade)"/>
      <path class="pocket" d="M620 310 H368 Q356 310 354 322 L346 413 H620 Z" fill="var(--paper-shade)"/>
    </svg>
    <div class="wordmark wordmark--pocket">
      <span class="wordmark__dot"></span>
      <div>
        <div class="wordmark__name">Brisk Estates</div>
        <div class="wordmark__tag">Property Management and Real Estate</div>
      </div>
    </div>
  </section>
</main>
</body>
</html>
```